Modern Banner for use on Emails and Electronic letters.

We need a Email banner that we can also uses as a banner on electronic documents . Would be a bonus to be able to use banner on pixmingle.
The banner should incorporate our logo and company name; The ProVela Group.
We would like an eye catching, modern design.
We are completely open to using colour and/or images along with our logo and company name.
Currently the font for our company name is time new roman but again we are open to suggestions. The company name can be be moved away from the umbrella logo to anywhere in the banner.

Industry/Entity Type

Electronic

Font styles to use
Serif
Sans Serif

Colors

Designer to choose colors to be used in the design.

Requirements
Must have
• ProVela Logo (Umbrella design - Black umbrella on red blocks with a letter on each block spelling VELA.
• Company name: The ProVela Group
• Be Modern and professional.
• Suitable for use as an email banner but can also be used as letterhead on electronic documents.
Nice to have
• Colour and/or images.
• Be able to be used as pixmingle banner.

```html
<!DOCTYPE html>
<html lang="en">
<head>
<meta charset="utf-8">
<title>The ProVela Group – Letterhead</title>
<link rel="stylesheet" href="https://fonts.googleapis.com/css2?family=Cormorant+Garamond:wght@600&display=swap">
<style>
  :root {
    --paper: #ffffff;
    --ink: #111111;
    --red: #e00000;
    --red-dark: #8c0000;
    --steel-dark: #3a3a3a;
    --steel: #a9b2b2;
    --steel-light: #f4f6f6;
  }
  html, body {
    margin: 0;
    padding: 0;
    overflow: hidden;
    background: var(--paper);
  }
  .letterhead {
    position: relative;
    width: 890px;
    height: 1200px;
    background: var(--paper);
    overflow: hidden;
  }
  .banner-bands {
    position: absolute;
    left: 0;
    top: 0;
    width: 780px;
    height: 112px;
  }
  .brand-mark {
    position: absolute;
    left: 128px;
    top: 36px;
    display: flex;
    align-items: center;
    gap: 6px;
    font-family: "Cormorant Garamond", "Times New Roman", serif;
    font-weight: 600;
    font-size: 24px;
    color: var(--red);
  }
  .brand-mark .mark-square {
    width: 12px;
    height: 12px;
    background: var(--red);
  }
  .company-name {
    position: absolute;
    left: 328px;
    width: 448px;
    top: 30px;
    margin: 0;
    text-align: center;
    font-family: "Cormorant Garamond", "Times New Roman", serif;
    font-weight: 600;
    color: var(--ink);
    line-height: 1;
    white-space: nowrap;
  }
  .company-name .minor { font-size: 32px; }
  .company-name .major { font-size: 50px; }
  .corner-decor {
    position: absolute;
    left: 781px;
    top: 0;
    width: 109px;
    height: 114px;
    background: linear-gradient(135deg, var(--red) 0%, var(--red-dark) 100%);
  }
  .footer-decor {
    position: absolute;
    left: 836px;
    top: 1170px;
    width: 34px;
    height: 30px;
    background: linear-gradient(90deg, var(--red) 0%, var(--red-dark) 100%);
  }
</style>
</head>
<body>
  <div class="letterhead">
    <svg class="banner-bands" viewBox="0 0 780 112" aria-hidden="true">
      <defs>
        <linearGradient id="band-left" x1="0" x2="1" y1="0" y2="0">
          <stop offset="0" stop-color="var(--steel-dark)"/>
          <stop offset="0.3" stop-color="var(--steel)"/>
          <stop offset="0.5" stop-color="var(--steel-light)"/>
          <stop offset="0.75" stop-color="var(--steel-light)"/>
          <stop offset="1" stop-color="var(--steel)"/>
        </linearGradient>
        <linearGradient id="band-main" x1="0" x2="1" y1="0" y2="0">
          <stop offset="0" stop-color="var(--steel-dark)"/>
          <stop offset="0.3" stop-color="var(--steel)"/>
          <stop offset="0.45" stop-color="var(--steel-light)"/>
          <stop offset="0.7" stop-color="var(--steel-light)"/>
          <stop offset="0.85" stop-color="var(--steel)"/>
          <stop offset="1" stop-color="var(--steel-light)"/>
        </linearGradient>
      </defs>
      <polygon points="0,0 324,12 324,110 0,90" fill="url(#band-left)"/>
      <polygon points="328,12 776,0 776,96 328,110" fill="url(#band-main)"/>
    </svg>

    <div class="brand-mark"><span class="mark-square"></span>ProVela</div>

    <h1 class="company-name"><span class="minor">The</span> <span class="major">ProVela</span> <span class="minor">Group</span></h1>

    <div class="corner-decor" role="img" aria-label="Decorative cluster of red 3D cubes"></div>
    <div class="footer-decor" role="img" aria-label="Small decorative red cube"></div>
  </div>
</body>
</html>
```